Take my logo and make me some cool looking business cards

I've got a logo that we've trademarked so you can't change the logo but you can change it's color combo and find a fun way to incorporate it into a new business card design that is fresh, stylish, and can be applied to some cool medium cost materials (plastic, wood, metal, etc). Basically, we're looking for business cards that stand out in a good way.
Here's the logo we're currently using:
Thanks to everyone that has submitted designs. We've narrowed down to the top 4 designs and tried to eliminate old versions or designs that just didn't match our vision as quickly as we could. We don't plan on keeping this open for the full 9 days; we plan on selecting a design in the next 48 hours; with the goal of having something in the hands of a printer, preferably plastic printer, by Thursday AM Pacific Time.
Business
- must include our existing logo

```html
<!DOCTYPE html>
<html lang="en">
<head>
<meta charset="utf-8">
<title>Halyard business card options</title>
<link href="https://fonts.googleapis.com/css2?family=Maven+Pro:wght@400;500;700&display=swap" rel="stylesheet">
<style>
  :root{
    --backdrop:#b9692f;
    --card-grey:#8c8c8c;
    --card-dark:#2b2b2b;
    --card-blue:#0e3e64;
    --panel-grey:#8f8f8f;
    --clear-strip:rgba(255,255,255,.42);
    --ink-white:#ffffff;
    --ink-navy:#1b4672;
    --mark-light:#b4b4b4;
    --mark-mid:#8a8a8a;
    --mark-gloss:#4d4d4d;
    --slot-tone:#c7783a;
    --note-ink:#333333;
  }
  *{box-sizing:border-box;margin:0;padding:0}
  html,body{width:731px;height:1200px;overflow:hidden}
  body{background:var(--backdrop);font-family:"Maven Pro",Arial,sans-serif;position:relative}

  .card{position:absolute;width:282px;height:161px;border-radius:42px 4px 42px 4px;overflow:hidden;background:var(--card-dark)}
  .card--grey{background:var(--card-grey)}
  .card--blue{background:var(--card-blue);border-radius:30px 4px 30px 4px}
  .card--front .brand{left:118px}
  .card--back .brand{left:0}

  .strip{position:absolute;left:0;right:0;height:12px;background:var(--clear-strip)}
  .strip--top{top:0}
  .strip--bottom{bottom:0}
  .card--back .strip{height:15px}

  .panel{position:absolute;left:0;right:0;top:15px;bottom:15px;background:var(--panel-grey)}

  .contact{position:absolute;left:0;width:128px;top:58px;text-align:center;color:var(--ink-white);font-size:7px;line-height:9.5px}
  .contact .name{font-weight:700;font-size:10px;line-height:13px;letter-spacing:.3px}
  .contact .role{font-weight:700;font-size:10px;line-height:13px;margin-bottom:6px}
  .contact .address{margin-bottom:3px}

  .brand{position:absolute;right:0;top:0;bottom:0;display:flex;align-items:center;justify-content:center;gap:7px;
    font-family:"Maven Pro",Arial,sans-serif;font-weight:500;font-size:21px;letter-spacing:1px;color:var(--ink-white)}
  .brand--navy{color:var(--ink-navy)}
  .mark{width:26px;height:26px;border-radius:50%;background:var(--mark-light);flex:none}
  .mark--mid{background:var(--mark-mid)}
  .mark--gloss{background:var(--mark-gloss)}

  .slots{position:absolute;left:36px;right:14px;height:7px;background:var(--slot-tone)}
  .slots--top{top:10px}
  .slots--bottom{bottom:10px;left:4px;right:30px}

  .note{position:absolute;font-size:21px;color:var(--note-ink)}
  .guides{position:absolute;left:0;top:0}
</style>
</head>
<body>

<!-- Row 1: clear plastic with frosted bands -->
<section class="card card--grey card--front" style="left:95px;top:32px">
  <div class="strip strip--top"></div><div class="strip strip--bottom"></div>
  <div class="contact"><p class="name">Dana Whitlow</p><p class="role">CEO</p><p>418 Marlow Street</p><p class="address">Cedar Cove, CA 94000</p><p>+15550104321</p><p>dw@halyard.com</p></div>
  <div class="brand brand--navy"><span class="mark"></span>HALYARD</div>
</section>
<section class="card card--grey card--back" style="left:392px;top:28px">
  <div class="strip strip--top"></div><div class="strip strip--bottom"></div>
  <div class="brand brand--navy"><span class="mark"></span>HALYARD</div>
</section>

<!-- Row 2: dark edges with grey middle -->
<section class="card card--front" style="left:95px;top:206px">
  <div class="panel"></div>
  <div class="contact"><p class="name">Dana Whitlow</p><p class="role">CEO</p><p>418 Marlow Street</p><p class="address">Cedar Cove, CA 94000</p><p>+15550104321</p><p>dw@halyard.com</p></div>
  <div class="brand"><span class="mark"></span>HALYARD</div>
</section>
<section class="card card--back" style="left:395px;top:203px">
  <div class="brand"><span class="mark mark--mid"></span>HALYARD</div>
</section>

<!-- Row 3: solid dark -->
<section class="card card--front" style="left:95px;top:382px">
  <div class="contact"><p class="name">Dana Whitlow</p><p class="role">CEO</p><p>418 Marlow Street</p><p class="address">Cedar Cove, CA 94000</p><p>+15550104321</p><p>dw@halyard.com</p></div>
  <div class="brand"><span class="mark mark--mid"></span>HALYARD</div>
</section>
<section class="card card--back" style="left:395px;top:380px">
  <div class="brand"><span class="mark mark--mid"></span>HALYARD</div>
</section>

<!-- Row 4: dark with lacquer accent -->
<section class="card card--front" style="left:95px;top:590px">
  <div class="contact"><p class="name">Dana Whitlow</p><p class="role">CEO</p><p>418 Marlow Street</p><p class="address">Cedar Cove, CA 94000</p><p>+15550104321</p><p>dw@halyard.com</p></div>
  <div class="brand"><span class="mark mark--gloss"></span>HALYARD</div>
</section>
<section class="card card--back" style="left:386px;top:588px">
  <div class="brand"><span class="mark mark--gloss"></span>HALYARD</div>
</section>

<!-- Row 5: navy -->
<section class="card card--blue card--front" style="left:102px;top:784px">
  <div class="contact" style="left:8px"><p class="name">Dana Whitlow</p><p class="role">CEO</p><p>418 Marlow Street</p><p class="address">Cedar Cove, CA 94000</p><p>+15550104321</p><p>dw@halyard.com</p></div>
  <div class="brand" style="left:126px"><span class="mark"></span>HALYARD</div>
</section>
<section class="card card--blue card--back" style="left:402px;top:780px">
  <div class="brand"><span class="mark"></span>HALYARD</div>
</section>

<!-- Row 6: dark with cut-out slot rows -->
<section class="card card--front" style="left:92px;top:994px">
  <div class="slots slots--top" role="img" aria-label="row of small cut-out slots"></div>
  <div class="slots slots--bottom" role="img" aria-label="row of small cut-out slots"></div>
  <div class="contact"><p class="name">Dana Whitlow</p><p class="role">CEO</p><p>418 Marlow Street</p><p class="address">Cedar Cove, CA 94000</p><p>+15550104321</p><p>dw@halyard.com</p></div>
  <div class="brand">HALYARD</div>
</section>
<section class="card card--back" style="left:393px;top:994px">
  <div class="slots slots--top" role="img" aria-label="row of small cut-out slots"></div>
  <div class="slots slots--bottom" role="img" aria-label="row of small cut-out slots"></div>
  <div class="brand">HALYARD</div>
</section>

<!-- Production notes -->
<p class="note" style="left:390px;top:558px">lacquer</p>
<p class="note" style="left:434px;top:955px">cut out</p>
<svg class="guides" width="731" height="1200" viewBox="0 0 731 1200" aria-hidden="true">
  <g stroke="#333" stroke-width="1" fill="none">
    <line x1="318" y1="624" x2="386" y2="578"/>
    <polyline points="378,578 386,578 382,585"/>
    <line x1="472" y1="570" x2="486" y2="575"/>
    <polyline points="478,569 472,570 476,575"/>
    <line x1="372" y1="1014" x2="438" y2="967"/>
    <polyline points="430,967 438,967 434,974"/>
  </g>
</svg>

</body>
</html>
```